VORLEN Website Design

We need a website designed for our company VORLEN. We are a luxury lifestyle club that will provide benefits and services for our members. The site should be clean & sleek, preferably using black and white (or darker colors). (example sites: brimvale.example, tusko.example)

Here is a link of a sample page I did using wix. (https://pelmundry4.sitebuild.example/mypage) This can be used to get a general idea.

Target Market(s)

Upper Middle Class in the United States

Number of Pages Required

5+ page

Font styles to use
Sans Serif
Other font styles liked:
• Arial (or other similar fonts)

Requirements
Must have
• A clean design that is eye-catching and speaks to our company.
Nice to have
• Ideas for copy.

```html
<!DOCTYPE html>
<html lang="en">
<head>
<meta charset="utf-8">
<title>VORLEN — Members Only Lifestyle Club</title>
<link rel="stylesheet" href="https://fonts.googleapis.com/css2?family=Montserrat:ital,wght@0,400;0,500;0,600;0,700;1,400&display=swap">
<style>
:root{
  --stage:#e6e6e6;
  --ink:#ffffff;
  --muted:#b9b9b9;
  --panel:#1c1c1c;
  --panel-2:#252525;
  --panel-3:#2e2e2e;
  --accent:#1565e0;
  --line:#3a3a3a;
}
*{box-sizing:border-box;margin:0;padding:0}
html,body{width:1200px;height:600px;overflow:hidden}
body{background:var(--stage);font-family:"Montserrat",Arial,sans-serif;color:var(--ink)}
.canvas{position:relative;width:1200px;height:600px;display:grid;grid-template-columns:570px 570px;grid-template-rows:280px 260px;gap:20px;padding:20px;justify-content:center;align-content:center}
.screen{position:relative;overflow:hidden;background:var(--panel);box-shadow:0 6px 18px rgba(0,0,0,.18)}

/* hero */
.hero-photo{position:absolute;inset:0 0 40px 0;background:linear-gradient(120deg,#3b3632 0%,#5a524b 45%,#2d2a28 100%)}
.hero-photo::after{content:"";position:absolute;inset:0;background:rgba(0,0,0,.35)}
.site-header{position:absolute;top:16px;left:22px;right:22px;display:flex;align-items:center;justify-content:space-between;z-index:2}
.brand{display:flex;align-items:center;gap:7px;font-size:15px;font-weight:600;letter-spacing:2px}
.brand-square{width:8px;height:8px;background:var(--accent)}
.main-nav{display:flex;align-items:center;gap:12px;font-size:7px;font-weight:600}
.main-nav .active{position:relative}
.main-nav .active::before{content:"";position:absolute;right:calc(100% + 4px);top:50%;width:16px;height:2px;background:var(--accent)}
.search-dot{width:10px;height:10px;border-radius:50%;background:var(--accent)}
.hero-title{position:absolute;top:112px;left:0;right:0;text-align:center;font-size:20px;font-weight:600;letter-spacing:.5px;z-index:2}
.hero-arrow{position:absolute;top:116px;z-index:2}
.hero-arrow.prev{left:22px}.hero-arrow.next{right:22px}
.hero-dots{position:absolute;bottom:54px;left:50%;transform:translateX(-50%);display:flex;gap:4px;z-index:2}
.hero-dots span{width:5px;height:5px;border-radius:50%;background:var(--muted)}
.hero-dots span:first-child{background:var(--ink)}
.hero-band{position:absolute;left:0;right:0;bottom:0;height:40px;background:var(--panel-2);text-align:center;padding-top:10px;font-size:16px;font-weight:500}
.band-notch{position:absolute;top:-10px;left:50%;transform:translateX(-50%)}

/* membership */
.membership-photo{position:absolute;left:0;right:0;top:0;height:150px;background:linear-gradient(160deg,#2a3a3e 0%,#1f4a66 55%,#3c4a4a 100%)}
.membership-photo::after{content:"";position:absolute;inset:0;background:rgba(0,0,0,.4)}
.membership-copy{position:absolute;top:36px;left:0;right:0;text-align:center;z-index:2}
.membership-copy .kicker{font-size:10px;font-weight:600;letter-spacing:1px}
.membership-copy h2{font-size:11px;font-weight:600;line-height:1.5;margin-top:3px;letter-spacing:.3px}
.btn-visit{display:inline-block;margin-top:12px;border:1px solid var(--ink);font-size:6px;font-weight:600;padding:4px 12px;letter-spacing:.5px}
.testimonials{position:absolute;top:150px;left:0;right:0;height:46px;background:var(--panel-2);text-align:center;padding-top:9px}
.testimonials h3{font-size:11px;font-weight:500;letter-spacing:.5px}
.testimonials p{font-size:7px;font-style:italic;color:var(--muted);margin-top:3px}
.testimonial-row{position:absolute;top:196px;left:0;right:0;bottom:0;display:flex;gap:14px;padding:8px 18px 0 18px}
.testimonial-photo{width:120px;height:72px;flex-shrink:0;background:linear-gradient(180deg,#9c8d76 0%,#e1b37a 55%,#59626b 100%)}
.testimonial-row p{flex:1;font-size:8px;line-height:1.7;color:#e6e6e6;padding-top:6px}

/* about */
.about-head{height:36px;text-align:center;font-size:15px;font-weight:500;padding-top:9px;background:var(--panel)}
.sub-nav{display:flex;justify-content:center;height:22px;background:var(--panel-2);font-size:6px}
.sub-nav span{padding:7px 12px;border-left:1px solid var(--line)}
.sub-nav span:last-child{border-right:1px solid var(--line)}
.about-body{display:flex;gap:18px;padding:14px 40px 0 40px;height:142px}
.lifestyle-photo{width:170px;height:70px;background:linear-gradient(180deg,#2d6ab0 0%,#b9916a 60%,#3b5a2a 100%);flex-shrink:0}
.lifestyle-copy h3{font-size:11px;font-weight:600;letter-spacing:.5px;margin-bottom:6px}
.lifestyle-copy p{font-size:6px;line-height:1.7;color:var(--muted)}
.team-intro{position:absolute;left:0;right:0;bottom:0;height:60px;background:var(--panel-2);text-align:center;padding-top:12px}
.team-intro h3{font-size:15px;font-weight:500}
.team-intro p{font-size:7px;font-style:italic;color:#dcdcdc;margin-top:4px}

/* team */
.team-grid{display:grid;grid-template-columns:repeat(4,1fr);gap:8px;padding:14px;height:100%;background:var(--panel)}
.member{background:var(--panel-2);display:flex;flex-direction:column;align-items:center}
.member.featured{background:var(--accent)}
.member-photo{width:100%;height:118px;background:linear-gradient(180deg,#4a4a4a 0%,#6b625c 60%,#2c2c2c 100%)}
.member.featured .member-photo{background:linear-gradient(180deg,#3d5f9c 0%,#2a63c6 100%)}
.chevron{margin-top:-11px;width:22px;height:22px}
.member-name{font-size:7px;font-weight:600;margin-top:6px;letter-spacing:.4px}
.member-rule{width:24px;height:1px;background:var(--ink);margin:5px 0}
.member-bio{font-size:5.5px;line-height:1.7;text-align:center;padding:0 8px;color:#e0e0e0}
.socials{display:flex;gap:4px;margin-top:6px}
.socials span{width:9px;height:9px;border-radius:50%;background:var(--ink)}
</style>
</head>
<body>
<main class="canvas">

  <section class="screen hero">
    <div class="hero-photo" role="img" aria-label="Photo of club members raising wine glasses at a dinner table"></div>
    <header class="site-header">
      <div class="brand"><span class="brand-square"></span>VORLEN</div>
      <nav class="main-nav">
        <span class="active">About us</span><span>Services &amp; Benefits</span><span>Contact</span><span class="search-dot"></span>
      </nav>
    </header>
    <svg class="hero-arrow prev" width="8" height="12" viewBox="0 0 8 12"><path d="M7 1 2 6l5 5" fill="none" stroke="#fff" stroke-width="2"/></svg>
    <h1 class="hero-title">A MEMBERS ONLY LIFESTYLE CLUB</h1>
    <svg class="hero-arrow next" width="8" height="12" viewBox="0 0 8 12"><path d="M1 1l5 5-5 5" fill="none" stroke="#fff" stroke-width="2"/></svg>
    <div class="hero-dots"><span></span><span></span><span></span></div>
    <div class="hero-band">
      <svg class="band-notch" width="24" height="10" viewBox="0 0 24 10"><path d="M0 10 12 0l12 10z" fill="#1565e0"/></svg>
      ABOUT US
    </div>
  </section>

  <section class="screen membership">
    <div class="membership-photo" role="img" aria-label="Photo of a resort pool terrace by the sea"></div>
    <div class="membership-copy">
      <div class="kicker">VORLEN</div>
      <h2>MEMBERSHIP PROVIDES YOU WITH AMAZING BENEFITS AND<br>SERVICES.</h2>
      <span class="btn-visit">VISIT</span>
    </div>
    <div class="testimonials">
      <h3>TESTIMONIALS</h3>
      <p>Dummy text of the printing and typesetting</p>
    </div>
    <div class="testimonial-row">
      <div class="testimonial-photo" role="img" aria-label="Photo of a sailing yacht at sunset"></div>
      <p>Lorem Ipsum is simply dummy text of the printing and typesetting industry. Lorem Ipsum has been the industry's standard dummy text ever since the 1500s.</p>
    </div>
  </section>

  <section class="screen about">
    <div class="about-head">ABOUT US</div>
    <nav class="sub-nav"><span>Services</span><span>Experiences</span><span>About VORLEN</span></nav>
    <div class="about-body">
      <div class="lifestyle-photo" role="img" aria-label="Photo of a lit luxury villa with palm trees at dusk"></div>
      <div class="lifestyle-copy">
        <h3>LIFESTYLE CLUB</h3>
        <p>Lorem ipsum dolor sit amet, consectetur adipiscing elit. Aenean egestas eu leo nec rhoncus. Nulla sapien turpis, convallis ac ultrices sed, aliquam sit amet eros. Donec consequat quam sit amet facilisis pharetra nisl.</p>
      </div>
    </div>
    <div class="team-intro">
      <h3>OUR TEAM</h3>
      <p>Morbi leo risus, porta ac consectetur ac, vestibulum at eros.</p>
    </div>
  </section>

  <section class="screen team">
    <div class="team-grid">
      <article class="member">
        <div class="member-photo" role="img" aria-label="Portrait photo of team member"></div>
        <svg class="chevron" viewBox="0 0 22 22"><circle cx="11" cy="11" r="11" fill="#1565e0"/><path d="M6.5 13 11 8.5l4.5 4.5" fill="none" stroke="#fff" stroke-width="2"/></svg>
        <div class="member-name">AREN TOLLEY</div><div class="member-rule"></div>
        <p class="member-bio">Morbi leo risus, porta ac consectetur ac, vestibulum at eros. Lorem ipsum dolor sit amet, consectetur adipiscing elit.</p>
      </article>
      <article class="member featured">
        <div class="member-photo" role="img" aria-label="Portrait photo of team member"></div>
        <svg class="chevron" viewBox="0 0 22 22"><circle cx="11" cy="11" r="11" fill="#0f4fb8"/><path d="M6.5 13 11 8.5l4.5 4.5" fill="none" stroke="#fff" stroke-width="2"/></svg>
        <div class="member-name">PELL ORRIN</div><div class="member-rule"></div>
        <p class="member-bio">Morbi leo risus, porta ac consectetur ac, vestibulum at eros. Lorem ipsum dolor sit amet.</p>
        <div class="socials"><span></span><span></span><span></span></div>
      </article>
      <article class="member">
        <div class="member-photo" role="img" aria-label="Portrait photo of team member"></div>
        <svg class="chevron" viewBox="0 0 22 22"><circle cx="11" cy="11" r="11" fill="#1565e0"/><path d="M6.5 13 11 8.5l4.5 4.5" fill="none" stroke="#fff" stroke-width="2"/></svg>
        <div class="member-name">MIRA DOSTEL</div><div class="member-rule"></div>
        <p class="member-bio">Morbi leo risus, porta ac consectetur ac, vestibulum at eros. Lorem ipsum dolor sit amet, consectetur adipiscing elit.</p>
      </article>
      <article class="member">
        <div class="member-photo" role="img" aria-label="Portrait photo of team member"></div>
        <svg class="chevron" viewBox="0 0 22 22"><circle cx="11" cy="11" r="11" fill="#1565e0"/><path d="M6.5 13 11 8.5l4.5 4.5" fill="none" stroke="#fff" stroke-width="2"/></svg>
        <div class="member-name">ILSE WARROW</div><div class="member-rule"></div>
        <p class="member-bio">Morbi leo risus, porta ac consectetur ac, vestibulum at eros. Lorem ipsum dolor sit amet, consectetur adipiscing elit.</p>
      </article>
    </div>
  </section>

</main>
</body>
</html>
```